Luxury Business Card Design

We need a business card design for a law firm that look sophisticated and luxury

Target Market(s)

Australian legal markets

Industry/Entity Type

Legal

Contact Information for Business Card

Attached

Requirements
Must have
• Logo, head office address on front side and 2 other addresses on the back side.
Nice to have
• Please see below our current business card. Need something more sophisticated and luxury feel

```html
<!DOCTYPE html>
<html lang="en">
<head>
<meta charset="utf-8">
<title>Ashby Lawyers – Business Card</title>
<link href="https://fonts.googleapis.com/css2?family=Inter:wght@300;400;700&family=Playfair+Display:wght@500;700&display=swap" rel="stylesheet">
<style>
  :root{
    --stage:#b2b2b2;
    --forest:#041b12;
    --forest-soft:#0a2a1d;
    --gold:#c9a86a;
    --gold-deep:#b8892d;
    --ink:#0f1512;
    --paper:#ffffff;
    --guide:#ffffff;
  }
  *{margin:0;padding:0;box-sizing:border-box}
  html,body{width:1200px;height:1140px;overflow:hidden;background:var(--stage)}
  body{position:relative;font-family:"Inter",Arial,sans-serif;color:var(--ink)}
  .card{position:absolute;left:275px;width:708px;height:424px;background:var(--paper);
        box-shadow:12px 18px 26px rgba(0,0,0,.35);overflow:hidden}
  .card--front{top:72px}
  .card--back{top:564px}

  /* front */
  .front-header{position:absolute;left:0;top:0;width:100%;height:214px;
        background:linear-gradient(160deg,var(--forest-soft),var(--forest) 70%)}
  .front-rule{position:absolute;left:0;top:214px;width:100%;height:4px;background:var(--gold-deep)}
  .front-strip{position:absolute;left:0;top:218px;width:100%;height:5px;background:var(--forest)}
  .brand{position:absolute;display:flex;flex-direction:column;align-items:center;transform:translateX(-50%)}
  .brand__ring{width:84px;height:84px;border:4px solid var(--gold-deep);border-radius:50%}
  .brand__name{margin-top:18px;font-family:"Playfair Display",Georgia,serif;font-weight:500;
        font-size:30px;letter-spacing:2px;color:var(--paper);white-space:nowrap}
  .card--front .brand{left:354px;top:31px}
  .card--back .brand{left:158px;top:137px}

  .person{position:absolute;left:0;width:301px;top:254px;text-align:center}
  .person__name{font-family:"Playfair Display",Georgia,serif;font-weight:700;font-size:34px;
        color:var(--gold);line-height:1;letter-spacing:.5px;white-space:nowrap}
  .person__role{margin-top:8px;font-weight:300;font-size:14px;line-height:21px;text-transform:uppercase}
  .divider{position:absolute;left:300px;top:244px;width:2px;height:104px;background:var(--gold-deep)}
  .contacts{position:absolute;left:327px;top:248px;list-style:none}
  .contacts li{display:flex;align-items:center;height:34px;font-size:17.5px;white-space:nowrap}
  .contacts svg{width:18px;height:18px;margin-right:14px;fill:var(--gold);flex:none}
  .address{position:absolute;left:0;width:100%;top:364px;text-align:center;font-size:17.5px;line-height:22px}
  .address svg{width:15px;height:19px;fill:var(--gold);vertical-align:-2px;margin-right:10px}

  /* back */
  .back-panel{position:absolute;left:0;top:0;width:317px;height:100%;background:var(--forest)}
  .back-rule{position:absolute;left:317px;top:0;width:3px;height:100%;background:var(--gold-deep)}
  .tagline{position:absolute;left:385px;top:36px;font-family:"Playfair Display",Georgia,serif;
        font-weight:500;font-size:27px;line-height:38px;color:var(--gold);text-transform:uppercase;white-space:nowrap}
  .office{position:absolute;left:386px;font-size:17.5px;line-height:21.5px;font-style:normal;white-space:nowrap}
  .office__city{font-weight:700;font-size:21px;line-height:26px}
  .office--east{top:194px}
  .office--west{top:316px}

  /* dimension guides */
  .guide{position:absolute;border:2px solid var(--guide)}
  .guide--height{left:228px;top:606px;width:26px;height:378px;border-right:none}
  .guide--width{left:291px;top:1024px;width:664px;height:30px;border-top:none}
  .guide-label{position:absolute;color:var(--guide);font-family:Arial,Helvetica,sans-serif;font-size:30px}
  .guide-label--height{left:65px;top:778px}
  .guide-label--width{left:552px;top:1084px}
</style>
</head>
<body>

<section class="card card--front">
  <div class="front-header" role="img" aria-label="Dark green header with fine diagonal pinstripe texture"></div>
  <div class="front-rule"></div>
  <div class="front-strip"></div>
  <div class="brand">
    <div class="brand__ring"></div>
    <div class="brand__name">ASHBY LAWYERS</div>
  </div>

  <div class="person">
    <div class="person__name">ALEX MORAN</div>
    <div class="person__role">Director &amp; Principal Solicitor<br>LLB, LLM</div>
  </div>
  <div class="divider"></div>
  <ul class="contacts">
    <li><svg viewBox="0 0 24 24"><path d="M15 3h3a2 2 0 0 1 2 2v14a2 2 0 0 1-2 2h-3v-5h2V8h-2z"/><path d="M9 7a5 5 0 0 0 0 10l1-1.5a3.5 3.5 0 0 1 0-7zM6 4a9 9 0 0 0 0 16l1-1.4a7.5 7.5 0 0 1 0-13.2z"/></svg>+61 7 3000 4120 &nbsp;/&nbsp; +61 0400 123 456</li>
    <li><svg viewBox="0 0 24 24"><path d="M2 5h20v14H2z" opacity=".9"/><path d="M2 5l10 8 10-8" fill="none" stroke="#fff" stroke-width="1.6"/></svg>alex@ashbylawyers.com.au</li>
    <li><svg viewBox="0 0 24 24"><circle cx="12" cy="12" r="10"/><path d="M2 12h20M12 2c-4 4-4 16 0 20M12 2c4 4 4 16 0 20" fill="none" stroke="#fff" stroke-width="1.4"/></svg>www.ashbylawyers.com.au</li>
  </ul>
  <p class="address"><svg viewBox="0 0 16 20"><path d="M8 0a8 8 0 0 0-8 8c0 6 8 12 8 12s8-6 8-12a8 8 0 0 0-8-8zm0 11a3 3 0 1 1 0-6 3 3 0 0 1 0 6z"/></svg>Level 2, Ashby House, 48 Kent Terrace,<br>Elmwood Heights, QLD 4105</p>
</section>

<section class="card card--back">
  <div class="back-panel"></div>
  <div class="back-rule"></div>
  <div class="brand">
    <div class="brand__ring"></div>
    <div class="brand__name">ASHBY LAWYERS</div>
  </div>
  <p class="tagline">Your Counsel<br>Your Outcome<br>Our Priority</p>
  <address class="office office--east">
    <div class="office__city">Eastbridge</div>
    Suite 110, Carlton Chambers<br>212 Harlow Lane<br>ELMSTEAD VIC 3012
  </address>
  <address class="office office--west">
    <div class="office__city">Westhaven</div>
    Suite 12, 64 Coastal Highway<br>CORALVALE WA 6021
  </address>
</section>

<div class="guide guide--height"></div>
<div class="guide-label guide-label--height">2 inches</div>
<div class="guide guide--width"></div>
<div class="guide-label guide-label--width">3.5 inches</div>

</body>
</html>
```